Book Cover Design Project - "Pass The Kettle"

"Pass the kettle - crafting tales to lift trade" is a business book that outlines what you need to know if you are planning to make videos for business communications.
The intended audience for the book is small to medium business owners. These are people who are keen to learn what they should know to do it themselves.
The cover needs to have a clear design that works as a thumbnail as well as full size.
Feel free to have some fun with it. It doesn't have to be all serious. Although this is a business book many people are afraid and don't know where to start with video production.
My company logo uses red, black, grey and white - www.brindlemoor.com.au . The logo has been uploaded.
It is not critical to use those elements, however if it can be incorporated into the design that's good too. The priority however is having a design that is eye catching.
The book will about 200 pages long. The back will include an authors photo, so blurb and testimonials- a word doc has been uploaded. It will also include the barcode, ISBN number, and price.
The spine will need to be clear and eyecatching as well.
The design should clearly reveal that this is about video production and provide a feeling of competency and comfort for those who read it.

The dimensions for the cover should be 12.8cm x 19.8cm.

At this point the spine thickness will be about 1.5cm x 19.8cm high

Please include my name on the front cover of the design:

Corin Walsby

The book is targeted to small to medium business owners who want to know how to make videos for their business. They are do it yourself people.

Business

• Front
Title: Pass the kettle
Tagline: Crafting tales to lift trade

I would also like the spine and back cover done as part of the design, however let's get the front done and then the rest can be completed based on the approved design.
• Pass the kettle is a play on words in regards to being filmed (shot) and the anxiety people feel about presenting in front of a camera.
One idea I've had (but I'm not attached to it), is to make the markings that are present in a camera's viewfinder to resemble those that are seen through the sights of a gun.
I'm really not attached to it and unless that can be achieved in a playful way, it is probably best to avoid.
• Please avoid images of low budget cameras. The impression we want here is that this is professional standard video production advice. (By the way you don't have to have any cameras at all).

Low budget cameras are handycams etc.

```html
<!DOCTYPE html>
<html lang="en">
<head>
<meta charset="utf-8">
<title>Pass The Kettle – Book Cover</title>
<link rel="stylesheet" href="https://fonts.googleapis.com/css2?family=Jost:wght@300;400&family=EB+Garamond&display=swap">
<style>
  :root {
    --red: #e01f25;
    --red-deep: #a8161c;
    --red-dark: #7a1014;
    --spine: #000000;
    --white: #ffffff;
    --white-soft: rgba(255,255,255,0.85);
    --ink: #111111;
  }
  * { margin: 0; padding: 0; box-sizing: border-box; }
  html, body { width: 1200px; height: 910px; overflow: hidden; background: var(--white); }
  .cover { position: relative; width: 1200px; height: 910px; }

  .back-cover, .front-cover, .spine { position: absolute; top: 0; height: 910px; }
  .back-cover { left: 0; width: 578px; }
  .spine { left: 578px; width: 43px; background: var(--spine); }
  .front-cover { left: 621px; width: 579px; }

  .back-photo {
    position: absolute; inset: 0;
    background:
      radial-gradient(ellipse 45% 12% at 40% 27%, rgba(122,16,20,0.35), transparent 70%),
      radial-gradient(ellipse 55% 20% at 50% 40%, rgba(122,16,20,0.45), transparent 70%),
      radial-gradient(ellipse 40% 18% at 20% 80%, rgba(168,22,28,0.55), transparent 70%),
      radial-gradient(ellipse 30% 22% at 75% 72%, rgba(122,16,20,0.4), transparent 70%),
      linear-gradient(180deg, var(--red) 0%, #e52227 45%, #cf1c22 100%);
  }
  .front-photo {
    position: absolute; inset: 0;
    background:
      radial-gradient(circle at 38% 17%, rgba(122,16,20,0.6) 0, rgba(168,22,28,0.4) 24%, transparent 40%),
      radial-gradient(ellipse 30% 20% at 20% 72%, rgba(122,16,20,0.35), transparent 70%),
      radial-gradient(ellipse 35% 25% at 85% 90%, rgba(122,16,20,0.5), transparent 70%),
      linear-gradient(180deg, #c41a20 0%, var(--red) 45%, var(--red-deep) 100%);
  }

  .barcode-area {
    position: absolute; left: 312px; top: 761px; width: 209px; height: 118px;
    background: var(--white);
    display: flex; align-items: center; justify-content: center;
    font-family: "EB Garamond", serif; font-size: 21px; color: var(--ink);
  }

  .spine-text {
    position: absolute; left: 0; top: 94px; width: 43px;
    writing-mode: vertical-rl;
    display: flex; align-items: center;
    font-family: "Jost", sans-serif; font-size: 21px; color: var(--white);
    white-space: nowrap; line-height: 43px;
  }
  .spine-title { font-weight: 300; letter-spacing: 0.5px; margin-bottom: 8px; }
  .spine-tagline { font-weight: 400; }

  .publisher {
    position: absolute; left: 199px; top: 52px; width: 190px;
    display: flex; flex-direction: column; align-items: center; gap: 8px;
  }
  .publisher-mark { width: 40px; height: 40px; border-radius: 50%; background: var(--white); }
  .publisher-name {
    font-family: "Jost", sans-serif; font-weight: 400; font-size: 25px;
    color: var(--white); letter-spacing: 0.5px;
  }

  .viewfinder {
    position: absolute; left: 48px; top: 360px; width: 484px; height: 250px;
  }
  .title {
    position: absolute; left: 40px; top: 382px; width: 500px;
    text-align: center;
    font-family: "Jost", sans-serif; font-weight: 300; font-size: 76px;
    line-height: 84px; color: var(--white); letter-spacing: 1px;
  }
  .author {
    position: absolute; left: 40px; top: 562px; width: 500px; text-align: center;
    font-family: "Jost", sans-serif; font-weight: 400; font-size: 24px;
    letter-spacing: 3px; color: var(--white-soft);
  }
  .tagline {
    position: absolute; left: 40px; top: 806px; width: 500px; text-align: center;
    font-family: "Jost", sans-serif; font-weight: 400; font-size: 30px;
    color: var(--white);
  }
</style>
</head>
<body>
<main class="cover">
  <section class="back-cover">
    <div class="back-photo" role="img" aria-label="Red-toned photograph of a blurred desk scene with large currency symbols"></div>
    <div class="barcode-area">Barcode Area</div>
  </section>

  <section class="spine">
    <div class="spine-text">
      <span class="spine-title">PASS THE KETTLE</span>
      <span class="spine-tagline">Crafting tales to lift trade</span>
    </div>
  </section>

  <section class="front-cover">
    <div class="front-photo" role="img" aria-label="Red-toned photograph of a globe clock with faint currency symbols"></div>
    <div class="publisher">
      <span class="publisher-mark"></span>
      <span class="publisher-name">BRINDLEMOOR</span>
    </div>
    <svg class="viewfinder" viewBox="0 0 484 250" aria-hidden="true">
      <g fill="none" stroke="#ffffff" stroke-width="2" stroke-opacity="0.8">
        <path d="M2 32 V2 H32"/>
        <path d="M452 2 H482 V32"/>
        <path d="M2 218 V248 H32"/>
        <path d="M452 248 H482 V218"/>
      </g>
      <circle cx="24" cy="24" r="6" fill="#ffffff" fill-opacity="0.85"/>
    </svg>
    <h1 class="title">PASS THE<br>KETTLE</h1>
    <p class="author">CORIN WALSBY</p>
    <p class="tagline">Crafting tales to lift trade</p>
  </section>
</main>
</body>
</html>
```